Qamra
قمرة كافيه
Hello Designers:-
Please check your e-mail inbox.
Thank you so much!
plz star rating...
The front and the back of the card should be one color "Beige". In front, it only shows the logo, the address, e-mail, twitter and instagram accounts. No need to type any other word like the word "قمرة"
As for the back, we want a loyalty card with 6 stamps with "Qamra" shape drawing on each. and the 6th qamra has a FREE written on it (Pic provided in brief)
If you have any comments, questions or requirements please do not hesitate to contact me on my e-mail or here, in the discussion.
Thank you so much for your work! :)
Hello designers: Please make sure to read the project brief as we want a (Double) sided business card/loyalty card. Moreover, please be aware that the card color should follow the color of the store "Beige" and not the logo color (Store pic provided in the brief)
Thank you so much for your effort! And good luck!

```html
<!DOCTYPE html>
<html lang="en">
<head>
<meta charset="utf-8">
<title>Qamra Stationery Set</title>
<link href="https://fonts.googleapis.com/css2?family=Lato:wght@400&display=swap" rel="stylesheet">
<style>
  :root {
    --beige: #c5a77c;
    --paper: #ffffff;
    --ink-light: #fbf6ee;
    --backdrop: #ffffff;
    --edge: #e2ddd5;
  }
  * { box-sizing: border-box; margin: 0; padding: 0; }
  html, body { width: 1200px; height: 778px; overflow: hidden; background: var(--backdrop); }
  body { position: relative; font-family: "Lato", sans-serif; color: var(--ink-light); }

  .piece { position: absolute; }
  .brand-name { font-family: "Lato", sans-serif; font-weight: 400; color: var(--ink-light); letter-spacing: 1px; display: flex; align-items: center; gap: 5px; white-space: nowrap; }
  .brand-dot { width: 6px; height: 6px; border-radius: 50%; background: var(--ink-light); }
  .contact { list-style: none; line-height: 1.55; color: var(--ink-light); white-space: nowrap; }

  /* Business card – front */
  .card-front { left: 101px; top: 149px; width: 216px; height: 132px; background: var(--beige); }
  .card-front .brand-name { position: absolute; left: 0; right: 0; top: 22px; justify-content: center; font-size: 15px; }
  .card-front .contact { position: absolute; left: 14px; top: 62px; font-size: 6px; }

  /* Business card – back (loyalty) */
  .card-back { left: 341px; top: 149px; width: 216px; height: 132px; background: var(--beige); }
  .stamp-numbers { position: absolute; top: 9px; left: 28px; width: 160px; display: flex; justify-content: space-around; font-size: 6px; }
  .stamp-row { position: absolute; top: 20px; left: 28px; width: 160px; display: flex; justify-content: space-between; }
  .stamp { width: 27px; height: 27px; border: 1px solid var(--ink-light); }
  .stamp-connector { position: absolute; left: 107px; top: 47px; width: 1px; height: 18px; background: var(--ink-light); }
  .stamp-free { position: absolute; left: 92px; top: 65px; width: 31px; height: 31px; border: 1px solid var(--ink-light); font-size: 6px; display: flex; align-items: flex-end; justify-content: center; padding-bottom: 3px; }
  .loyalty-note { position: absolute; left: 0; right: 0; bottom: 10px; text-align: center; font-size: 7px; letter-spacing: 1.5px; }

  /* Envelope */
  .envelope { left: 67px; top: 329px; width: 533px; height: 278px; background: var(--paper); border: 1px solid var(--edge); }
  .envelope-band { position: absolute; left: 0; top: 0; width: 100%; height: 163px; background: var(--beige); }
  .envelope-flap-line { position: absolute; left: 0; top: 58px; width: 100%; height: 1px; background: rgba(255,255,255,0.35); }
  .envelope .brand-name.flap-mark { position: absolute; left: 0; right: 0; top: 16px; justify-content: center; font-size: 14px; }
  .envelope .brand-name.side-mark { position: absolute; left: 14px; top: 96px; font-size: 12px; }
  .envelope .contact { position: absolute; left: 84px; top: 74px; font-size: 6.5px; }

  /* Letterhead */
  .letterhead { left: 638px; top: 34px; width: 490px; height: 696px; background: var(--paper); border: 1px solid var(--edge); }
  .letterhead-band { position: absolute; left: 0; top: 0; width: 100%; height: 115px; background: var(--beige); }
  .letterhead .brand-name { position: absolute; left: 14px; top: 44px; font-size: 13px; }
  .letterhead .contact { position: absolute; left: 88px; top: 14px; font-size: 6.5px; }
</style>
</head>
<body>

  <section class="piece card-front" aria-label="Business card front">
    <div class="brand-name"><span class="brand-dot"></span>Qamra</div>
    <ul class="contact">
      <li>Qamra Cafe, Tahlia St, Jeddah</li>
      <li>+966 12 555 0142</li>
      <li>hello@qamra-house.com</li>
      <li>@toldamer7</li>
      <li>@qamra.house</li>
    </ul>
  </section>

  <section class="piece card-back" aria-label="Loyalty card back">
    <div class="stamp-numbers"><span>1</span><span>2</span><span>3</span><span>4</span><span>5</span></div>
    <div class="stamp-row">
      <div class="stamp"></div><div class="stamp"></div><div class="stamp"></div><div class="stamp"></div><div class="stamp"></div>
    </div>
    <div class="stamp-connector"></div>
    <div class="stamp-free">Free</div>
    <p class="loyalty-note">Buy 5 and get the 6th one free</p>
  </section>

  <section class="piece envelope" aria-label="Envelope">
    <div class="envelope-band"></div>
    <div class="envelope-flap-line"></div>
    <div class="brand-name flap-mark"><span class="brand-dot"></span>Qamra</div>
    <div class="brand-name side-mark">Qamra</div>
    <ul class="contact">
      <li>Qamra Cafe, Tahlia St, Jeddah</li>
      <li>+966 12 555 0142</li>
      <li>hello@qamra-house.com</li>
      <li>@toldamer7</li>
      <li>@qamra.house</li>
    </ul>
  </section>

  <section class="piece letterhead" aria-label="Letterhead">
    <div class="letterhead-band"></div>
    <div class="brand-name">Qamra</div>
    <ul class="contact">
      <li>Qamra Cafe, Tahlia St, Jeddah</li>
      <li>+966 12 555 0142</li>
      <li>hello@qamra-house.com</li>
      <li>@toldamer7</li>
      <li>@qamra.house</li>
    </ul>
  </section>

</body>
</html>
```